Retractable Banner Design for Retail Shopping Event

I need a design for a 33” by 86” retractable banner. It should have my logo at the top (the largest element of the design) and the banner should also include my website and Instagram handle:
www.mirabelhtx.com
@mirabelhtx
I have included product pictures in the brief that can be used. I also included different versions of my logo file, including AI. I need the file to be ready to upload to my printer.
My store is an upscale women’s boutique. I am also attaching designs I have selected in the past to give an idea of my aesthetic.

```html
<!DOCTYPE html>
<html lang="en">
<head>
<meta charset="utf-8">
<title>Mirabel HTX – Retractable Banner</title>
<link rel="stylesheet" href="https://fonts.googleapis.com/css2?family=Marcellus&family=Montserrat:wght@400;800&display=swap">
<style>
  :root {
    --page: #ffffff;
    --ink: #0b0b0b;
    --blush: #ecd2cd;
    --slate: #5c605f;
    --bag-tone: #d9bcae;
    --gold: #d4b15a;
    --tray-gold: #e6cf86;
    --slipper: #a08e9a;
    --pom: #ecd1c0;
  }
  * { margin: 0; padding: 0; box-sizing: border-box; }
  html, body { width: 900px; height: 1200px; overflow: hidden; background: var(--page); }
  .sheet { position: relative; width: 900px; height: 1200px; }
  .spec-note {
    position: absolute; top: 118px; left: 0; width: 900px; text-align: center;
    font-family: "Montserrat", sans-serif; font-weight: 800; font-size: 37px;
    letter-spacing: 0.5px; color: var(--ink);
  }
  .banner {
    position: absolute; left: 279px; top: 218px; width: 342px; height: 891px;
    background: var(--blush); overflow: hidden;
  }
  .brand-frame { position: absolute; left: 48px; top: 65px; width: 246px; height: 86px; }
  .brand-name {
    position: absolute; left: 0; top: 15px; width: 100%; text-align: center;
    font-family: "Marcellus", serif; font-size: 44px; line-height: 50px;
    letter-spacing: 2px; color: var(--slate);
  }
  .brand-sub {
    position: absolute; left: 0; top: 77px; width: 100%; text-align: center;
    font-family: "Marcellus", serif; font-size: 13px; line-height: 16px;
    letter-spacing: 1.5px; color: var(--slate);
  }
  .products { position: absolute; left: 0; top: 0; width: 342px; height: 891px; }
  .contact-frame { position: absolute; left: 47px; top: 736px; width: 248px; height: 60px; }
  .contact-web {
    position: absolute; left: 0; top: 12px; width: 100%; text-align: center;
    font-family: "Marcellus", serif; font-size: 19px; line-height: 22px;
    letter-spacing: 0.5px; color: var(--slate);
  }
  .contact-social {
    position: absolute; left: 0; top: 48px; width: 100%; display: flex; justify-content: center;
    align-items: center; gap: 8px;
    font-family: "Marcellus", serif; font-size: 18px; line-height: 22px; color: var(--slate);
  }
  .social-dot { width: 20px; height: 20px; border-radius: 50%; background: var(--slate); }
</style>
</head>
<body>
<div class="sheet">
  <p class="spec-note">FILE SIZE IS 33 X 86</p>

  <section class="banner">
    <div class="brand-frame">
      <svg width="246" height="86" viewBox="0 0 246 86">
        <path d="M85 85 H1 V1 H245 V85 H161" fill="none" stroke="var(--slate)" stroke-width="1.5"/>
      </svg>
      <div class="brand-name">MIRABEL</div>
      <div class="brand-sub">HTX</div>
    </div>

    <svg class="products" viewBox="0 0 342 891">
      <defs>
        <linearGradient id="bagFill" x1="0" y1="0" x2="1" y2="1">
          <stop offset="0" stop-color="#e6cdc0"/><stop offset="1" stop-color="var(--bag-tone)"/>
        </linearGradient>
        <radialGradient id="trayFill"><stop offset="0.6" stop-color="var(--tray-gold)"/><stop offset="1" stop-color="#c9a650"/></radialGradient>
        <linearGradient id="slipperFill" x1="0" y1="0" x2="1" y2="1">
          <stop offset="0" stop-color="var(--pom)"/><stop offset="1" stop-color="var(--slipper)"/>
        </linearGradient>
      </defs>
      <path role="img" aria-label="Product photo: satin blush tote bag with snake print"
            d="M0 210 L130 240 L215 330 L120 512 L0 470 Z" fill="url(#bagFill)"/>
      <g role="img" aria-label="Product photo: gold flower stud earrings with crystals">
        <circle cx="256" cy="263" r="48" fill="var(--gold)" opacity="0.55"/>
        <circle cx="342" cy="335" r="27" fill="var(--gold)" opacity="0.55"/>
      </g>
      <ellipse role="img" aria-label="Product photo: round leopard print lacquer tray"
               cx="342" cy="524" rx="160" ry="104" fill="url(#trayFill)"/>
      <path role="img" aria-label="Product photo: lilac slippers with blush pom poms"
            d="M0 595 C45 560 140 520 185 600 C195 650 175 710 120 705 C65 700 22 690 0 680 Z"
            fill="url(#slipperFill)"/>
    </svg>

    <div class="contact-frame">
      <svg width="248" height="60" viewBox="0 0 248 60">
        <path d="M48 59 H1 V1 H247 V59 H200" fill="none" stroke="var(--slate)" stroke-width="1.5"/>
      </svg>
      <div class="contact-web">www.mirabelhtx.com</div>
      <div class="contact-social"><span class="social-dot"></span><span>@mirabelhtx</span></div>
    </div>
  </section>
</div>
</body>
</html>
```